Modern and Vibrant Car Wash Website

In Summary: A website using our Menus for Exterior and Full Service Car Washes: Meadowlark, tidewater car wash, Vireo and Copperleaf Express Car Wash websites (link attached below are good references for the type of cartoony fun design).

I will add our flyer, and menus, and some other graphics as a visual reference. Will over time add the files (AI and SVG so you can use them).

Car wash front page should be nice and clean. I have lots of videos and photos we can use throughout the wash. Would like a video on the landing page.

Our shop section can remain blank as my POS developers will create a hyperlink to it.

Main easy to use functions should be the Car Wash services, their price and full service ones as well. Allow customers to see, book if needed etc.

Please note I have the website on PLOM.

I have attached a general pdf as well for some more info.

https://meadowlarkgleamwash.ca/
https://tidewatercarwash.ca/
https://marblecarwash.com/
https://vireowash.com/
https://plainpagebuilder.com/carwash-website-design/
https://copperleafexpresscarwash.com/

```html
<!DOCTYPE html>
<html lang="en">
<head>
<meta charset="UTF-8">
<title>Gleamway Car Wash</title>
<link rel="stylesheet" href="https://fonts.googleapis.com/css2?family=Montserrat:wght@400;500;600;700&display=swap">
<style>
  :root {
    --blue: #0a5291;
    --blue-bright: #0b63b0;
    --yellow: #f5c518;
    --yellow-deep: #e7b30c;
    --text: #6b6b6b;
    --line: #0b63b0;
    --white: #ffffff;
  }
  * { box-sizing: border-box; margin: 0; padding: 0; }
  html, body { width: 1200px; height: 4096px; overflow: hidden; }
  body {
    position: relative;
    font-family: 'Montserrat', sans-serif;
    background: var(--white);
    color: var(--text);
  }
  .abs { position: absolute; }

  /* Header */
  .site-header { left: 0; top: 0; width: 1200px; height: 92px; background: var(--white); z-index: 3; }
  .brand { left: 100px; top: 28px; display: flex; align-items: center; gap: 10px;
    font-weight: 700; font-size: 22px; color: var(--blue); }
  .brand-dot { width: 22px; height: 22px; border-radius: 50%; background: var(--yellow); }
  .main-nav { left: 372px; top: 34px; display: flex; gap: 36px; font-size: 17px; font-weight: 500; color: var(--blue); }
  .header-btn { left: 941px; top: 24px; width: 159px; height: 44px; border-radius: 6px; background: var(--blue-bright);
    color: var(--white); font-size: 16px; font-weight: 600; display: flex; align-items: center; justify-content: center; }
  .header-rule { left: 100px; top: 91px; width: 1100px; height: 3px;
    background: linear-gradient(90deg, rgba(11,99,176,0), var(--line) 40%, rgba(11,99,176,0.2)); z-index: 4; }

  /* Hero */
  .hero-photo { left: 254px; top: 92px; width: 946px; height: 658px;
    background:
      linear-gradient(90deg, #fff 0%, rgba(255,255,255,0.6) 12%, rgba(255,255,255,0) 30%),
      linear-gradient(180deg, rgba(255,255,255,0) 75%, rgba(255,255,255,0.5) 100%),
      radial-gradient(ellipse at 62% 45%, #f2d44a 0%, #dcc25a 25%, #b9b2a3 55%, #8e8f8f 100%); }
  .tag { height: 27px; padding: 0 14px; border: 2px solid var(--blue-bright); border-radius: 14px;
    font-size: 15px; font-weight: 700; color: var(--blue); display: inline-flex; align-items: center; background: var(--white); }
  .hero-tag { left: 100px; top: 188px; }
  .hero-title { left: 100px; top: 228px; font-size: 70px; line-height: 77px; font-weight: 700; color: var(--blue); }
  .hero-sub { left: 100px; top: 398px; font-size: 20px; font-weight: 600; color: var(--blue); }
  .btn-yellow { height: 56px; padding: 0 30px; border-radius: 8px; background: var(--yellow);
    border: 2px solid var(--yellow-deep); box-shadow: 0 4px 0 rgba(11,99,176,0.25);
    font-size: 20px; font-weight: 600; color: var(--blue);
    display: inline-flex; align-items: center; gap: 12px; }
  .hero-btn { left: 100px; top: 464px; width: 230px; justify-content: center; }

  /* Split sections */
  .photo { border-radius: 4px; }
  .photo-wash { left: 100px; top: 833px; width: 475px; height: 434px;
    background: radial-gradient(ellipse at 60% 55%, #2b2d31 0%, #55585c 45%, #7c7f82 80%, #5f5a44 100%); }
  .section-title { font-size: 41px; line-height: 51px; font-weight: 700; color: var(--blue); }
  .intro-title { left: 625px; top: 833px; width: 480px; }
  .body-text { font-size: 14px; line-height: 24px; color: var(--text); }
  .intro-text { left: 625px; top: 1004px; width: 480px; }
  .checklist { list-style: none; }
  .checklist li { display: flex; align-items: center; gap: 14px; height: 37.5px; font-size: 14px; color: var(--text); }
  .tick { width: 19px; height: 19px; flex: none; }
  .intro-list { left: 625px; top: 1085px; }

  /* Centered headings */
  .center-block { left: 0; width: 1200px; text-align: center; }
  .center-text { font-size: 14px; line-height: 24px; color: var(--text); }

  /* Cards */
  .card { width: 321px; border: 2px solid var(--blue-bright); border-radius: 8px; background: var(--white); text-align: center; }
  .service-card { top: 1691px; height: 318px; padding: 32px 14px 0; }
  .icon-badge { width: 66px; height: 66px; border-radius: 50%; background: var(--yellow);
    margin: 0 auto; display: flex; align-items: center; justify-content: center; }
  .card-title { font-size: 21px; line-height: 29px; font-weight: 700; color: var(--blue); margin-top: 20px; }
  .card-text { font-size: 13.5px; line-height: 24px; color: var(--text); margin-top: 18px; }

  .features-tag { left: 100px; top: 2178px; }
  .features-title { left: 100px; top: 2225px; width: 480px; }
  .features-text { left: 100px; top: 2395px; width: 480px; }
  .features-btn { left: 100px; top: 2509px; width: 230px; justify-content: center; }
  .photo-car { left: 625px; top: 2177px; width: 475px; height: 434px;
    background: radial-gradient(ellipse at 50% 60%, #d9dadb 0%, #9a9b9c 30%, #5b4d44 65%, #2c2624 100%); }
  .section-rule { left: 100px; top: 2695px; width: 1000px; height: 3px;
    background: linear-gradient(90deg, rgba(11,99,176,0), var(--line) 50%, rgba(11,99,176,0)); }

  /* Packages */
  .package-card { top: 2989px; height: 453px; padding: 32px 20px 0; }
  .package-card .card-title { margin-top: 22px; }
  .package-card .checklist { text-align: left; margin-top: 10px; padding-left: 2px; }
  .package-card .checklist li { font-size: 13.5px; }
  .package-rule { height: 2px; background: var(--blue-bright); margin: 12px 0 0; }
  .price { display: flex; justify-content: center; align-items: flex-start; color: var(--blue); font-weight: 700; margin-top: 14px; }
  .price .cur { font-size: 20px; margin-top: 4px; margin-right: 8px; }
  .price .whole { font-size: 50px; line-height: 56px; }
  .price .cents { font-size: 20px; margin-top: 4px; margin-left: 10px; }
  .package-card.popular { background: var(--yellow); }
  .package-card.popular .icon-badge { background: var(--blue-bright); }
  .package-card.popular .checklist li { color: var(--blue); }
  .popular-pill { left: 541px; top: 2976px; width: 120px; height: 26px; border-radius: 13px; background: var(--blue-bright);
    color: var(--white); font-size: 13px; font-weight: 600; display: flex; align-items: center; justify-content: center; z-index: 2; }

  /* App */
  .app-title { left: 100px; top: 3611px; width: 535px; font-size: 38px; white-space: nowrap; }
  .app-text { left: 100px; top: 3730px; width: 480px; }
  .app-btn { left: 100px; top: 3844px; width: 266px; justify-content: center; }
  .phone { left: 642px; top: 3594px; width: 431px; height: 560px; border: 18px solid #2a2a2c; border-bottom: none;
    border-radius: 70px 70px 0 0; background: var(--white); }
  .phone-notch { left: 795px; top: 3625px; width: 125px; height: 36px; border-radius: 18px; background: #111; }
  .phone-title { left: 693px; top: 3713px; font-size: 31px; line-height: 40px; font-weight: 600; color: var(--blue); }
  .phone-text { left: 693px; top: 3807px; width: 330px; font-size: 14px; line-height: 24px; color: var(--blue-bright); }
  .phone-rule { left: 693px; top: 3924px; width: 326px; height: 2px; background: var(--blue-bright); }
  .phone-circle { left: 744px; top: 3946px; width: 228px; height: 228px; border-radius: 50%; background: #eef0f3;
    display: flex; justify-content: center; padding-top: 60px; }
</style>
</head>
<body>
<svg width="0" height="0" style="position:absolute">
  <defs>
    <symbol id="tick-yellow" viewBox="0 0 20 20"><circle cx="10" cy="10" r="10" fill="#f5c518"/><path d="M5.5 10.3l3 3 6-6.3" fill="none" stroke="#fff" stroke-width="2" stroke-linecap="round" stroke-linejoin="round"/></symbol>
    <symbol id="tick-blue" viewBox="0 0 20 20"><circle cx="10" cy="10" r="10" fill="#0b63b0"/><path d="M5.5 10.3l3 3 6-6.3" fill="none" stroke="#fff" stroke-width="2" stroke-linecap="round" stroke-linejoin="round"/></symbol>
    <symbol id="icon-flag" viewBox="0 0 24 24"><path d="M5 21V4M5 4h13l-2.5 4.5L18 13H5" fill="none" stroke="currentColor" stroke-width="2" stroke-linejoin="round"/><path d="M8 4v9M11 4v9M14 4v9" stroke="currentColor" stroke-width="1.2"/></symbol>
    <symbol id="icon-calendar" viewBox="0 0 24 24"><rect x="4" y="5" width="16" height="15" rx="2" fill="none" stroke="currentColor" stroke-width="2"/><path d="M4 9h16M8 3v4M16 3v4M9 14l2 2 4-4" fill="none" stroke="currentColor" stroke-width="2" stroke-linecap="round"/></symbol>
    <symbol id="icon-clipboard" viewBox="0 0 24 24"><rect x="5" y="4" width="14" height="17" rx="2" fill="none" stroke="currentColor" stroke-width="2"/><rect x="9" y="2.5" width="6" height="3.5" rx="1" fill="currentColor"/><path d="M8.5 10h7M8.5 13.5h7M8.5 17h5" stroke="currentColor" stroke-width="1.8" stroke-linecap="round"/></symbol>
  </defs>
</svg>

<header class="site-header abs">
  <div class="brand abs"><span class="brand-dot"></span>Gleamway</div>
  <nav class="main-nav abs"><span>Home</span><span>Find a wash</span><span>Join the club</span><span>Gift cards</span></nav>
  <div class="header-btn abs">Get free wash</div>
</header>
<div class="header-rule abs"></div>

<section class="hero">
  <div class="hero-photo abs" role="img" aria-label="Attendant in a yellow shirt hand-drying a car at a full service wash station"></div>
  <span class="tag hero-tag abs">Caledons' first</span>
  <h1 class="hero-title abs">Full service<br>car wash</h1>
  <p class="hero-sub abs">Interior &amp; exterior</p>
  <a class="btn-yellow hero-btn abs">Get free wash <span>→</span></a>
</section>

<section class="intro">
  <div class="photo photo-wash abs" role="img" aria-label="Dark sedan being sprayed inside an automatic wash tunnel"></div>
  <h2 class="section-title intro-title abs">Keeping Your Car Clean is Easy and Affordable</h2>
  <p class="body-text intro-text abs">Tired of driving a dirty car but don't have the time or tools to keep it clean? At Tidewater Car Wash, we make car care simple, fast, and effective. We offer everything you need to keep your.</p>
  <ul class="checklist intro-list abs">
    <li><svg class="tick"><use href="#tick-yellow"/></svg>11 Convenient Locations</li>
    <li><svg class="tick"><use href="#tick-yellow"/></svg>Free Vacuums</li>
    <li><svg class="tick"><use href="#tick-yellow"/></svg>Specialized Services</li>
    <li><svg class="tick"><use href="#tick-yellow"/></svg>Daily Wash Club Memberships</li>
    <li><svg class="tick"><use href="#tick-yellow"/></svg>Excellent Customer Service</li>
  </ul>
</section>

<section class="services">
  <div class="center-block abs" style="top:1436px"><span class="tag">Services</span></div>
  <h2 class="section-title center-block abs" style="top:1481px">Find Your Perfect Wash<br>&amp; Nearest Location</h2>
  <p class="center-text center-block abs" style="top:1601px">Pick the service that fits your car's needs, and we'll show you the closest Tidewater Car<br>Wash! It's easy, quick, and the first step to a cleaner, happier ride!</p>

  <article class="card service-card abs" style="left:100px">
    <div class="icon-badge" style="color:var(--blue-bright)"><svg width="26" height="26"><use href="#icon-flag"/></svg></div>
    <h3 class="card-title">Maintain your car's<br>resale value</h3>
    <p class="card-text">Praesent praesent ipsum ac pharetra venenatis. Nisi enim nullam id malesuada quis laoreet convallis. Vulputate sed amet tortor elit urna nibh.</p>
  </article>
  <article class="card service-card abs" style="left:439px">
    <div class="icon-badge" style="color:var(--blue-bright)"><svg width="26" height="26"><use href="#icon-calendar"/></svg></div>
    <h3 class="card-title">Maintain your car's<br>resale value</h3>
    <p class="card-text">Praesent praesent ipsum ac pharetra venenatis. Nisi enim nullam id malesuada quis laoreet convallis. Vulputate sed amet tortor elit urna nibh.</p>
  </article>
  <article class="card service-card abs" style="left:778px">
    <div class="icon-badge" style="color:var(--blue-bright)"><svg width="26" height="26"><use href="#icon-clipboard"/></svg></div>
    <h3 class="card-title">Find Your Perfect Wash<br>&amp; Nearest Location</h3>
    <p class="card-text">Praesent praesent ipsum ac pharetra venenatis. Nisi enim nullam id malesuada quis laoreet convallis. Vulputate sed amet tortor elit urna nibh.</p>
  </article>
</section>

<section class="features">
  <span class="tag features-tag abs">Features</span>
  <h2 class="section-title features-title abs">Keeping Your Car Clean is Easy and Affordable</h2>
  <p class="body-text features-text abs">Tired of driving a dirty car but don't have the time or tools to keep it clean? At Tidewater Car Wash, we make car care simple, fast, and effective. We offer everything you need to keep your.</p>
  <a class="btn-yellow features-btn abs">Get free wash <span>→</span></a>
  <div class="photo photo-car abs" role="img" aria-label="White sports car surrounded by spray mist in a wash bay at night"></div>
</section>
<div class="section-rule abs"></div>

<section class="packages">
  <div class="center-block abs" style="top:2784px"><span class="tag">Packages</span></div>
  <h2 class="section-title center-block abs" style="top:2829px">See our packages</h2>
  <p class="center-text center-block abs" style="top:2897px">Pick the service that fits your car's needs, and we'll show you the closest Tidewater Car<br>Wash! It's easy, quick, and the first step to a cleaner, happier ride!</p>

  <article class="card package-card abs" style="left:100px">
    <div class="icon-badge" style="color:var(--blue-bright)"><svg width="26" height="26"><use href="#icon-flag"/></svg></div>
    <h3 class="card-title">Ultimate ceramic shine</h3>
    <ul class="checklist">
      <li><svg class="tick"><use href="#tick-yellow"/></svg>Bumper blaster</li>
      <li><svg class="tick"><use href="#tick-yellow"/></svg>Tripple soap</li>
      <li><svg class="tick"><use href="#tick-yellow"/></svg>Reel &amp; wheel cleaner</li>
      <li><svg class="tick"><use href="#tick-yellow"/></svg>Under spray with rust inhibitor</li>
      <li><svg class="tick"><use href="#tick-yellow"/></svg>Daily Wash Club Memberships</li>
    </ul>
    <div class="package-rule"></div>
    <div class="price"><span class="cur">$</span><span class="whole">25</span><span class="cents">99</span></div>
  </article>

  <div class="popular-pill abs">Most popular</div>
  <article class="card package-card popular abs" style="left:439px">
    <div class="icon-badge" style="color:var(--white)"><svg width="26" height="26"><use href="#icon-calendar"/></svg></div>
    <h3 class="card-title">Signature shine</h3>
    <ul class="checklist">
      <li><svg class="tick"><use href="#tick-blue"/></svg>Bumper blaster</li>
      <li><svg class="tick"><use href="#tick-blue"/></svg>Daily Wash Club Memberships</li>
      <li><svg class="tick"><use href="#tick-blue"/></svg>Daily Wash Club Memberships</li>
      <li><svg class="tick"><use href="#tick-blue"/></svg>Daily Wash Club Memberships</li>
      <li><svg class="tick"><use href="#tick-blue"/></svg>Daily Wash Club Memberships</li>
    </ul>
    <div class="package-rule"></div>
    <div class="price"><span class="cur">$</span><span class="whole">17</span><span class="cents">99</span></div>
  </article>

  <article class="card package-card abs" style="left:778px">
    <div class="icon-badge" style="color:var(--blue-bright)"><svg width="26" height="26"><use href="#icon-clipboard"/></svg></div>
    <h3 class="card-title">Pro shine</h3>
    <ul class="checklist">
      <li><svg class="tick"><use href="#tick-yellow"/></svg>Bumper blaster</li>
      <li><svg class="tick"><use href="#tick-yellow"/></svg>Tripple soap</li>
      <li><svg class="tick"><use href="#tick-yellow"/></svg>Reel &amp; wheel cleaner</li>
      <li><svg class="tick"><use href="#tick-yellow"/></svg>Under spray with rust inhibitor</li>
      <li><svg class="tick"><use href="#tick-yellow"/></svg>Daily Wash Club Memberships</li>
    </ul>
    <div class="package-rule"></div>
    <div class="price"><span class="cur">$</span><span class="whole">13</span><span class="cents">99</span></div>
  </article>
</section>

<section class="app">
  <h2 class="section-title app-title abs">Download the<br>tidewater car wash app</h2>
  <p class="body-text app-text abs">Tired of driving a dirty car but don't have the time or tools to keep it clean? At Tidewater Car Wash, we make car care simple, fast, and effective. We offer everything you need to keep your.</p>
  <a class="btn-yellow app-btn abs">Download the app</a>

  <div class="phone abs"></div>
  <div class="phone-notch abs"></div>
  <h3 class="phone-title abs">Get easy with<br>your wash</h3>
  <p class="phone-text abs">Tired of driving a dirty car but don't have the time or tools to keep it clean? At Tidewater Car Wash, we make car care simple, fast, and effective. We offer everything you.</p>
  <div class="phone-rule abs"></div>
  <div class="phone-circle abs" style="color:#c9ced6"><svg width="110" height="110"><use href="#icon-clipboard"/></svg></div>
</section>
</body>
</html>
```